Bright Path Attorneys Billboard Design for Personal Injury Law Firm

Need a billboard design that we can use for different versions. 1400px X 400px jpeg or png
I have attached the logo and the attorney for the billboard. Attorney Marla Benning
Here is a link to our current website brightpathlegalgroup.example

HEADLINE: HIT BY A TRUCK?
SUBHEAD: NO FEE. BIG FIGHT.
877-GRANTLY

HEADLINE: ACCIDENT?
SUBHEAD: NO FEE, UNLESS WE WIN!
877-GRANTLY

HEADLINE: BIG TRUCK. BIG CASE.
SUBHEAD: YOU PAY $0 UPFRONT
877-GRANTLY

Target Market(s)

People in Car Accident

Industry/Entity Type

Personal Injury Attorneys

```html
<!DOCTYPE html>
<html lang="en">
<head>
<meta charset="utf-8">
<title>Bright Path Attorneys – Billboard</title>
<link href="https://fonts.googleapis.com/css2?family=Anton&family=Roboto+Condensed:wght@500;700&display=swap" rel="stylesheet">
<style>
  :root {
    --page-bg: #e9edf1;
    --board-light: #f4f1ec;
    --board-warm: #efe3d2;
    --ink: #141414;
    --brand-green: #5cab3c;
    --photo-dark: #2b2f35;
    --photo-mid: #7c858f;
    --photo-light: #c9ccd0;
    --white: #ffffff;
  }
  * { margin: 0; padding: 0; box-sizing: border-box; }
  html, body {
    width: 1200px; height: 1020px; overflow: hidden;
    background: var(--page-bg);
  }
  .billboard {
    position: absolute; left: 40px; top: 334px;
    width: 1120px; height: 352px; overflow: hidden;
    background: linear-gradient(90deg, var(--board-light) 0%, var(--board-light) 35%, var(--board-warm) 52%);
  }
  .crash-photo {
    position: absolute; left: 470px; top: 0; width: 650px; height: 352px;
    background:
      radial-gradient(ellipse at 22% 35%, rgba(255,236,200,0.85) 0%, rgba(255,236,200,0) 45%),
      linear-gradient(90deg, rgba(239,227,210,0) 0%, var(--photo-light) 28%, var(--photo-mid) 48%, var(--photo-dark) 72%, var(--photo-mid) 100%);
  }
  .crash-photo::before {
    content: ""; position: absolute; inset: 0;
    background: linear-gradient(180deg, rgba(30,30,34,0.35) 0%, rgba(0,0,0,0) 40%, rgba(20,20,24,0.55) 100%);
  }
  .headline {
    position: absolute; left: 49px; top: 42px;
    font-family: "Anton", "Impact", sans-serif;
    color: var(--ink); line-height: 1; text-transform: uppercase;
  }
  .headline__main { display: block; font-size: 67px; letter-spacing: 1px; }
  .headline__sub { display: block; font-size: 45px; letter-spacing: 0.5px; margin-top: 8px; }
  .brand {
    position: absolute; left: 45px; top: 282px;
    display: flex; align-items: center; gap: 12px;
  }
  .brand__mark { width: 34px; height: 34px; background: var(--brand-green); }
  .brand__name {
    font-family: "Roboto Condensed", "Arial Narrow", sans-serif;
    font-weight: 500; font-size: 27px; color: var(--ink); white-space: nowrap;
  }
  .phone {
    position: absolute; left: 350px; top: 284px;
    font-family: "Roboto Condensed", "Arial Narrow", sans-serif;
    font-weight: 700; font-size: 40px; color: var(--ink); line-height: 1;
  }
  .web-band {
    position: absolute; left: 639px; top: 283px; width: 481px; height: 45px;
    background: var(--brand-green);
    display: flex; align-items: center; justify-content: center;
    font-family: "Roboto Condensed", "Arial Narrow", sans-serif;
    font-weight: 700; font-size: 24px; color: var(--white);
  }
</style>
</head>
<body>
  <section class="billboard" aria-label="Bright Path Attorneys billboard">
    <div class="crash-photo" role="img" aria-label="Close-up of a silver car with a crushed front end after a collision, sunlit street behind"></div>
    <h1 class="headline">
      <span class="headline__main">Hit by a truck?</span>
      <span class="headline__sub">No fee. Big fight.</span>
    </h1>
    <div class="brand">
      <span class="brand__mark"></span>
      <span class="brand__name">Bright Path Attorneys</span>
    </div>
    <div class="phone">877-GRANTLY</div>
    <div class="web-band">brightpathlegalgroup.example</div>
  </section>
</body>
</html>
```